BRAMBLE CABS

Taxi card design

Need changes very slow in replying to my messages.

Target Market(s)

Customers

Industry/Entity Type

Taxi

Contact Information for Business Card

See previous design

Font styles to use
Sans Serif

Colors
A7469A
B969AE
D3A5CF
EDDBEB
F8F0F9
6B429C
8869AF
B7A5CE
E3DAEB
F3F0F8

Requirements
Nice to have
• We are in the business of looking after people, not just driving vehicles front
Should not have
• Front number 01832 419 526 needs to big big

```html
<!DOCTYPE html>
<html lang="en">
<head>
<meta charset="utf-8">
<title>Bramble Cabs – Business Card</title>
<link rel="stylesheet" href="https://fonts.googleapis.com/css2?family=Poppins:wght@300;400;500;600;700&display=swap">
<style>
  :root {
    --plum: #6B429C;
    --plum-mid: #8869AF;
    --plum-soft: #B7A5CE;
    --orchid: #A7469A;
    --orchid-mid: #B969AE;
    --orchid-soft: #D3A5CF;
    --ink: #2b2630;
    --paper: #f7f6f8;
    --backdrop: #e4e3e6;
    --white: #ffffff;
  }
  * { box-sizing: border-box; margin: 0; padding: 0; }
  html, body {
    width: 1200px; height: 900px; overflow: hidden;
    background: var(--backdrop);
    font-family: "Poppins", sans-serif;
  }
  .card {
    position: absolute; top: 200px;
    width: 500px; height: 500px;
    border-radius: 4px;
    overflow: hidden;
  }
  .card--front { left: 70px; background: var(--paper); color: var(--ink); }
  .card--back { left: 630px; }

  .services {
    position: absolute; top: 44px; right: 40px;
    font-size: 13px; font-weight: 400; letter-spacing: 0.3px;
    color: var(--plum-mid);
  }
  .services .divider { margin: 0 6px; color: var(--plum); }
  .address {
    position: absolute; top: 74px; right: 40px;
    text-align: right; font-size: 13px; line-height: 1.5;
  }
  .brand {
    position: absolute; left: 52px; top: 200px;
  }
  .brand__name {
    font-size: 36px; font-weight: 700; color: var(--plum);
    letter-spacing: 0.5px; line-height: 1;
  }
  .brand__tagline {
    margin-top: 8px; margin-left: 120px;
    font-size: 19px; font-weight: 600; color: var(--ink);
  }
  .email {
    position: absolute; left: 52px; top: 318px;
    font-size: 16px; font-weight: 400;
  }
  .phone {
    position: absolute; left: 40px; top: 358px;
    padding: 12px 22px;
    border-radius: 12px;
    background: linear-gradient(90deg, var(--plum), var(--orchid));
    color: var(--white);
    font-size: 42px; font-weight: 600; letter-spacing: 0.5px; line-height: 1.1;
  }

  .back__photo {
    position: absolute; inset: 0;
    background:
      radial-gradient(ellipse at 80% 10%, var(--orchid-soft) 0%, transparent 45%),
      linear-gradient(160deg, var(--orchid) 0%, var(--orchid-mid) 30%, var(--plum-mid) 65%, var(--plum) 100%);
  }
  .back__brand {
    position: absolute; left: 0; right: 0; top: 190px;
    text-align: center; color: var(--white);
  }
  .back__name { font-size: 40px; font-weight: 700; letter-spacing: 0.5px; line-height: 1; }
  .back__since { margin-top: 10px; font-size: 13px; font-weight: 300; letter-spacing: 1px; }
  .back__tagline { margin-top: 8px; font-size: 20px; font-weight: 600; }
</style>
</head>
<body>
  <section class="card card--front">
    <p class="services">AIRPORT TRANSFERS<span class="divider">|</span>MINIBUSES<span class="divider">|</span>SCHOOL TRANSPORT</p>
    <p class="address">Orchard Mews Hall, Millbrook Rd Thornley<br>TL14 6QA</p>
    <div class="brand">
      <p class="brand__name">BRAMBLE CABS</p>
      <p class="brand__tagline">24/7 Service</p>
    </div>
    <p class="email">bramblecabs@mailbox.co.uk</p>
    <p class="phone">01832 419 526</p>
  </section>

  <section class="card card--back">
    <div class="back__photo" role="img" aria-label="Soft-focus night photo of a taxi roof sign with blurred city lights, tinted pink and purple"></div>
    <div class="back__brand">
      <p class="back__name">BRAMBLE CABS</p>
      <p class="back__since">Established since 1986</p>
      <p class="back__tagline">24/7 Service</p>
    </div>
  </section>
</body>
</html>
```